Executive Business Card for Healthcare Company [Need Today]

I need a business card design for a healthcare company. The only branding the company has thus far is a logo. The cards will be utilized by company executives. The design I envision will be vibrant and appealing but with a corporate feel. They shouldn't be too casual or playful. I would like to complete this project TODAY if possible.

Target Market(s)

Healthcare vendors, other executives in healthcare and pharmaceuticals

Industry/Entity Type

Pharmaceutical

Contact Information for Business Card

See attachment

Font styles to use
Serif
Sans Serif

Colors

Designer to choose colors to be used in the design.

```html
<!DOCTYPE html>
<html lang="en">
<head>
<meta charset="utf-8">
<title>Calder Therapeutics – Business Card</title>
<link rel="stylesheet" href="https://fonts.googleapis.com/css2?family=Work+Sans:wght@300;400;500;600&display=swap">
<style>
  :root {
    --backdrop: #d4d8d9;
    --card-white: #f3f3f1;
    --teal: #1fb3b8;
    --teal-dark: #179ea3;
    --ink: #2c2f30;
    --ink-soft: #4a4e50;
    --white: #ffffff;
  }
  * { margin: 0; padding: 0; box-sizing: border-box; }
  html, body {
    width: 1200px; height: 900px; overflow: hidden;
    background: var(--backdrop);
    font-family: "Work Sans", Arial, sans-serif;
  }
  .canvas {
    width: 1200px; height: 900px;
    display: flex; flex-direction: column;
    align-items: center; justify-content: center; gap: 40px;
  }
  .card {
    width: 700px; height: 400px;
    position: relative;
    box-shadow: 0 10px 28px rgba(0,0,0,0.12);
  }
  .card-front { background: var(--card-white); color: var(--ink); }
  .card-back {
    background: var(--teal);
    display: flex; align-items: center; justify-content: center;
  }

  .brand { display: flex; align-items: center; gap: 14px; }
  .brand-dot {
    border-radius: 50%;
    border: 2px solid currentColor;
    flex: none;
  }
  .brand-name { font-weight: 400; letter-spacing: 0.02em; }

  .card-front .brand {
    position: absolute; left: 48px; top: 40px; color: var(--teal);
  }
  .card-front .brand-dot { width: 52px; height: 52px; }
  .card-front .brand-name { font-size: 26px; }

  .card-back .brand { color: var(--white); gap: 22px; }
  .card-back .brand-dot { width: 120px; height: 120px; border-width: 3px; }
  .card-back .brand-name { font-size: 46px; font-weight: 300; }

  .contact-list {
    position: absolute; left: 48px; top: 170px;
    list-style: none; font-size: 17px; line-height: 27px; color: var(--ink-soft);
  }
  .contact-list li { display: flex; align-items: center; gap: 12px; }
  .contact-list svg { width: 13px; height: 13px; fill: none; stroke: var(--teal); stroke-width: 1.6; }

  .person {
    position: absolute; right: 48px; top: 150px; text-align: right;
  }
  .person-name { font-size: 27px; font-weight: 600; color: var(--teal); }
  .person-title { font-size: 15px; color: var(--ink-soft); margin-top: 4px; }

  .company-address {
    position: absolute; right: 48px; bottom: 40px; text-align: right;
    font-style: normal; font-size: 16px; line-height: 23px; color: var(--ink-soft);
  }
  .company-legal { color: var(--teal); }
</style>
</head>
<body>
<main class="canvas">
  <section class="card card-front" aria-label="Business card front">
    <div class="brand">
      <span class="brand-dot"></span>
      <span class="brand-name">Calder Therapeutics</span>
    </div>

    <ul class="contact-list">
      <li>
        <svg viewBox="0 0 12 12"><path d="M2 1.5 L4.5 1.5 L5.2 4 L3.8 5 Q5 7.5 7 8.2 L8 6.8 L10.5 7.5 L10.5 10 Q5 10.5 1.5 4 Z"/></svg>
        555-210-4837
      </li>
      <li>
        <svg viewBox="0 0 12 12"><rect x="3" y="1" width="6" height="10" rx="1"/><line x1="5.3" y1="9.2" x2="6.7" y2="9.2"/></svg>
        555-672-1904
      </li>
      <li>
        <svg viewBox="0 0 12 12"><rect x="1" y="2.5" width="10" height="7"/><path d="M1 2.5 L6 6.5 L11 2.5"/></svg>
        mvossler@calderrx.com
      </li>
    </ul>

    <div class="person">
      <p class="person-name">Maren Vossler</p>
      <p class="person-title">Senior Director of Marketing</p>
    </div>

    <address class="company-address">
      <span class="company-legal">Calder Therapeutics, LLC</span><br>
      118 W Linden Avenue<br>
      Marlow, GA 30999
    </address>
  </section>

  <section class="card card-back" aria-label="Business card back">
    <div class="brand">
      <span class="brand-dot"></span>
      <span class="brand-name">Calder Therapeutics</span>
    </div>
  </section>
</main>
</body>
</html>
```